Willowmere Spa and Beauty Ltd. (Name of business)

I need a business card designed for this new company based out of Toronto Ontario. We specialize in Eyelash Extensions, Manicures and Pedicures, body waxing, massages, laser hair removal and botox treatments. Also offer a variety of products for sale, such as skin cream serums, collagen gel, eye cream, etc. It is a safe relaxing and non-judgemental environnment. Clients are welcome to come be pampered for the half or full day. Many service packages to choose from.

Open 7days per week from 8am to 8pm.

Priscilla Dunmore
Spa Facilitator
Willowmere Spa and Beauty Ltd.
7200 Harcourt St; Suite 1400
Toronto ON K2P 9W4

OFFICE: 416.790.4100
FAX: 416.790.4101
CELL: 416.632.1987
EMAIL: priscilla.dunmore@willowmerespa.com

Target Market(s)

Target market is primarily female ranging from 16 years old to 50 years old.

Industry/Entity Type

Business

Contact Information for Business Card

Priscilla Dunmore
Spa Facilitator
7200 Harcourt St; Suite 1400
Toronto ON K2P 9W4

OFFICE: 416.790.4100
FAX: 416.790.4101
CELL: 416.632.1987

Logo Text

I dont have a logo yet. I would like it simple but sophisticated and modern.

Font styles to use
Serif

Requirements
Must have
• all pertinent details such as company name, logo, name and contact information, services that are offered, including package rates
Nice to have
• Company name and logo prominent. A card that is neat and the information such as address, phone number, fax, email, etc is not too crowded but laid out in an easy to read format.
• Possibly on the back of card - some of the services offered could be listed, as well as professional cream lotions and serums. Hours of operation etc.

```html
<!DOCTYPE html>
<html lang="en">
<head>
<meta charset="utf-8">
<title>Willowmere Spa and Beauty Ltd. — Business Card</title>
<link rel="stylesheet" href="https://fonts.googleapis.com/css2?family=Cormorant+Garamond:wght@500&family=Lato:wght@400;700&display=swap">
<style>
  :root {
    --backdrop: #2a2c30;
    --card-black: #1f1f21;
    --card-white: #ffffff;
    --spa-pink: #e6359a;
    --text-light: #f2f2f2;
    --text-muted: #d8d8d8;
    --body-font: "Lato", Arial, sans-serif;
    --name-font: "Cormorant Garamond", Georgia, serif;
  }
  * { box-sizing: border-box; margin: 0; padding: 0; }
  html, body { width: 1200px; height: 900px; overflow: hidden; }
  body {
    background: var(--backdrop);
    font-family: var(--body-font);
    position: relative;
  }
  .card {
    position: absolute;
    top: 300px;
    width: 520px;
    height: 297px;
    border-radius: 22px;
    overflow: hidden;
    box-shadow: 0 10px 30px rgba(0,0,0,0.45);
  }

  /* Front */
  .card-front { left: 50px; background: var(--card-white); }
  .front-dark {
    position: absolute; left: 0; top: 0; bottom: 0; width: 262px;
    background: var(--card-black);
  }
  .front-band {
    position: absolute; left: 0; right: 0; top: 84px; height: 92px;
    background: var(--spa-pink);
  }
  .person {
    position: absolute; left: 24px; top: 22px;
  }
  .person-name {
    font-size: 22px; font-weight: 700; color: var(--text-light); line-height: 1.1;
  }
  .person-name .surname { color: var(--spa-pink); }
  .person-title {
    font-size: 11px; color: var(--text-muted); margin-top: 2px;
    padding-bottom: 4px; border-bottom: 2px solid var(--spa-pink); width: 92px;
  }
  .address {
    position: absolute; left: 24px; top: 106px;
    font-size: 12px; line-height: 1.45; color: var(--text-light);
  }
  .address svg { vertical-align: -2px; margin-right: 5px; }
  .address .address-line2 { padding-left: 15px; }
  .band-brand {
    position: absolute; left: 276px; right: 12px; top: 104px;
    color: var(--text-light); white-space: nowrap;
  }
  .brand-name {
    font-family: var(--name-font); font-weight: 500; font-size: 17px; line-height: 1.15;
  }
  .hours { font-size: 11.5px; margin-top: 8px; }
  .contacts {
    position: absolute; left: 22px; top: 190px;
    list-style: none; font-size: 11px; line-height: 1.85; color: var(--text-muted);
    white-space: nowrap;
  }
  .contacts svg { vertical-align: -2px; margin-right: 7px; }

  /* Back */
  .card-back { left: 630px; background: var(--card-black); }
  .back-brand {
    position: absolute; left: 40px; right: 30px; top: 54px;
    font-family: var(--name-font); font-weight: 500; font-size: 34px;
    color: var(--spa-pink); text-align: center; white-space: nowrap;
  }
  .services {
    position: absolute; left: 44px; top: 120px;
    border-left: 4px solid var(--spa-pink); padding-left: 12px;
    list-style: none; font-size: 11.5px; line-height: 1.6; color: var(--spa-pink);
  }
</style>
</head>
<body>
  <section class="card card-front" aria-label="Business card front">
    <div class="front-dark"></div>
    <div class="front-band"></div>

    <div class="person">
      <p class="person-name">Priscilla <span class="surname">Dunmore</span></p>
      <p class="person-title">Spa Facilitator</p>
    </div>

    <p class="address">
      <svg width="10" height="12" viewBox="0 0 10 12" aria-hidden="true"><path d="M5 11.5C2 8 1 6.2 1 4.5a4 4 0 0 1 8 0C9 6.2 8 8 5 11.5z" fill="none" stroke="#fff" stroke-width="1.2"/><circle cx="5" cy="4.5" r="1.4" fill="#fff"/></svg>7200 Harcourt St; Suite 1400<br>
      <span class="address-line2">Toronto On K2P 9W4</span>
    </p>

    <div class="band-brand">
      <p class="brand-name">Willowmere Spa and Beauty Ltd.</p>
      <p class="hours">Open 7days per week from 8am to 8pm</p>
    </div>

    <ul class="contacts">
      <li><svg width="9" height="12" viewBox="0 0 9 12" aria-hidden="true"><rect x="1" y="0.6" width="7" height="10.8" rx="1.2" fill="none" stroke="#e6359a" stroke-width="1.2"/></svg>416 632 1987</li>
      <li><svg width="10" height="10" viewBox="0 0 10 10" aria-hidden="true"><path d="M2 1l2 2-1 1.5c.6 1.2 1.3 1.9 2.5 2.5L7 6l2 2-1.5 1.5C4 9 1 6 .5 2.5z" fill="#e6359a"/></svg>416 790 4100</li>
      <li><svg width="10" height="10" viewBox="0 0 10 10" aria-hidden="true"><rect x="0.6" y="3" width="8.8" height="6" rx="1" fill="none" stroke="#e6359a" stroke-width="1.2"/><rect x="2.5" y="0.6" width="5" height="3" fill="none" stroke="#e6359a" stroke-width="1.1"/></svg>416 790 4101</li>
      <li><svg width="11" height="9" viewBox="0 0 11 9" aria-hidden="true"><rect x="0.6" y="0.6" width="9.8" height="7.8" fill="none" stroke="#e6359a" stroke-width="1.2"/><path d="M0.6 0.6l4.9 4 4.9-4" fill="none" stroke="#e6359a" stroke-width="1.2"/></svg>priscilla.dunmore@willowmerespa.com</li>
    </ul>
  </section>

  <section class="card card-back" aria-label="Business card back">
    <p class="back-brand">Willowmere Spa and Beauty Ltd.</p>
    <ul class="services">
      <li>Manicures and Pedicures | body waxing</li>
      <li>Removal and botox treatments | laser hair</li>
      <li>Eyelash Extensions | massages</li>
    </ul>
  </section>
</body>
</html>
```